Website redesign www.brindlecovepc.com law firm site

Need to redesign the website that I currently have to look more modern and professional. Would also like to be able to make updates and post without having a huge hassle. See current www.brindlecovepc.com. I just think that it looks very immature and it's very templated there's no ability for me to make posts or Add links or anything like that

Target Market(s)

California people looking for a powerhouse attorney in

Industry/Entity Type

Legal

Number of Pages Required

3 page

Font styles to use
Serif
Sans Serif

Colors
ec1f27
000000
ffffff

Requirements
Must have
• Must be mobile friendly. Must look professional and have ability to post links to other websites. Must have ability to post blogs or articles. Would like to be able to read my Quindral account and also have the ability to upload forms for people to download
Nice to have
• Simple design easy to use and not cluttered with too much text

```html
<!DOCTYPE html>
<html lang="en">
<head>
<meta charset="utf-8">
<title>Brindle Cove P.C</title>
<link href="https://fonts.googleapis.com/css2?family=Tinos&family=Montserrat:wght@400;500;600;700&family=Open+Sans:wght@400;600&display=swap" rel="stylesheet">
<style>
:root{
  --red:#e2232a;
  --black:#000;
  --ink:#222;
  --muted:#666;
  --white:#fff;
  --pale:#f1f1f1;
  --dark:#3a3a3a;
  --footer:#161616;
  --footer-text:#cfcfcf;
}
*{margin:0;padding:0;box-sizing:border-box}
html,body{width:1200px;height:2946px;overflow:hidden;background:var(--white)}
body{position:relative;font-family:"Open Sans",sans-serif;color:var(--ink)}
.abs{position:absolute}
.serif{font-family:"Tinos",serif}

/* header */
.site-header{left:0;top:0;width:1200px;height:105px;background:#f4f0ea}
.brand{left:60px;top:30px;display:flex;align-items:center;gap:12px;white-space:nowrap;font-family:"Montserrat",sans-serif;font-weight:600;font-size:27px;color:var(--ink)}
.brand-mark{width:18px;height:18px;background:var(--red)}
.top-contact{top:12px;font-family:"Montserrat",sans-serif;font-size:16px;color:var(--ink);display:flex;align-items:center;gap:10px;white-space:nowrap}
.round-ico{width:28px;height:28px;border-radius:50%;background:var(--red);display:flex;align-items:center;justify-content:center}
.main-nav{right:60px;top:66px;display:flex;gap:36px;font-family:"Montserrat",sans-serif;font-size:15px;font-weight:500;color:var(--ink)}
.main-nav .active{position:relative}
.main-nav .active::after{content:"";position:absolute;left:0;right:0;top:26px;height:3px;background:var(--red)}

/* hero */
.hero{left:0;top:105px;width:1200px;height:517px;background:linear-gradient(90deg,#f1e8d8 0%,#d9c4a1 40%,#9a6a3c 70%,#5b3a20 100%)}
.hero-title{left:60px;top:238px;font-size:46px;line-height:56px;color:#1e1a16;font-weight:400}
.hero-sub{left:60px;top:356px;font-size:17px;color:#2b2520}
.btn{background:var(--red);color:var(--white);font-family:"Montserrat",sans-serif;font-weight:600;display:flex;align-items:center;justify-content:center}
.hero-btn{left:60px;top:401px;width:138px;height:43px;font-size:16px}

/* welcome */
.section-title{left:0;width:1200px;text-align:center;font-family:"Tinos",serif;color:var(--black);font-size:31px;font-weight:400}
.section-sub{left:0;width:1200px;text-align:center;font-size:13px;color:var(--muted)}
.practice{top:850px;width:250px;text-align:center}
.practice svg{display:block;margin:0 auto}
.practice-rule{width:100px;height:1px;background:#999;margin:18px auto 0}
.practice h3{font-family:"Montserrat",sans-serif;font-weight:500;font-size:17px;margin-top:10px;color:var(--ink)}
.practice p{font-size:13px;line-height:21px;color:var(--muted);margin-top:14px}

/* consultation */
.consult-photo{left:0;top:1195px;width:600px;height:480px;background:linear-gradient(135deg,#d8d2cb 0%,#b69b86 45%,#6e5b50 100%)}
.consult-panel{left:600px;top:1195px;width:600px;height:480px;background:var(--pale)}
.consult-title{left:640px;top:1226px;font-size:31px;color:var(--red);font-weight:400;white-space:nowrap}
.consult-sub{left:642px;top:1276px;font-size:14px;color:var(--muted)}
.field{background:var(--white);border:1px solid #ddd}
.send-btn{left:643px;top:1567px;width:139px;height:44px;background:#1b1b1b;color:var(--white);font-family:"Montserrat",sans-serif;font-size:15px;font-weight:500;display:flex;align-items:center;justify-content:center}

/* testimonials */
.t-card{background:var(--white);box-shadow:0 6px 22px rgba(0,0,0,.14);text-align:center}
.t-card.faded{opacity:.22}
.avatar{border-radius:50%;background:linear-gradient(135deg,#d9b48f,#7a5a3e);margin:0 auto}
.t-card p{color:var(--ink)}
.t-name{background:var(--red);color:var(--white);font-family:"Montserrat",sans-serif;font-weight:500;margin:0 auto;display:flex;align-items:center;justify-content:center}
.dots{left:553px;top:2266px;display:flex;gap:14px;align-items:center}
.dot{width:6px;height:6px;border-radius:50%;background:#bbb}
.dot.on{width:14px;height:14px;background:var(--red)}

/* call band */
.call-band{left:0;top:2400px;width:1200px;height:110px;background:var(--dark)}
.call-red{left:0;top:2390px;width:440px;height:120px}
.call-help{left:127px;top:2432px;color:var(--white);font-family:"Montserrat",sans-serif;font-weight:700;font-size:21px;line-height:26px}
.call-now{left:545px;top:2440px;color:var(--white);font-family:"Montserrat",sans-serif;font-weight:600;font-size:21px;white-space:nowrap}
.call-now b{font-size:30px;font-weight:600}
.join-btn{left:1001px;top:2437px;width:138px;height:43px;background:var(--white);color:var(--black);font-family:"Montserrat",sans-serif;font-weight:700;font-size:16px;display:flex;align-items:center;justify-content:center}

/* footer */
.site-footer{left:0;top:2510px;width:1200px;height:436px;background:var(--footer)}
.f-head{top:2555px;color:var(--white);font-family:"Montserrat",sans-serif;font-weight:600;font-size:16px}
.f-row{color:var(--footer-text);font-size:13px;display:flex;gap:14px;align-items:flex-start;line-height:22px}
.news{left:342px;color:var(--footer-text);font-size:13px}
.news i{display:block;font-size:9px;color:#888;margin-top:4px}
.about{left:613px;top:2605px;width:255px;color:var(--footer-text);font-size:12px;line-height:26px}
.about-brand{left:613px;top:2745px;display:flex;align-items:center;gap:8px;color:var(--white);font-family:"Montserrat",sans-serif;font-weight:600;font-size:20px}
.about-brand span{width:12px;height:12px;background:var(--white)}
.qf{left:882px;width:235px;background:#2a2a2a;border:1px solid #333;color:#aaa;font-size:11px;padding:8px 12px}
.f-send{left:882px;top:2803px;width:98px;height:39px;font-size:16px}
.socials{left:75px;top:2777px;display:flex;gap:11px}
.socials span{width:28px;height:28px;border-radius:50%;border:1px solid #555}
.f-line{left:60px;top:2888px;width:1080px;height:1px;background:#333}
.copy{left:0;top:2910px;width:1200px;text-align:center;color:var(--footer-text);font-size:12px;font-family:"Montserrat",sans-serif}
</style>
</head>
<body>

<header class="site-header abs">
  <div class="brand abs"><span class="brand-mark"></span>Brindle Cove P.C</div>
  <div class="top-contact abs" style="left:757px">
    <span class="round-ico"><svg width="14" height="14" viewBox="0 0 14 14"><rect x="1" y="3" width="12" height="8" fill="none" stroke="#fff" stroke-width="1.5"/><path d="M1 3 L7 8 L13 3" fill="none" stroke="#fff" stroke-width="1.5"/></svg></span>1-800-555-0142
  </div>
  <div class="top-contact abs" style="left:936px">
    <span class="round-ico"><svg width="14" height="14" viewBox="0 0 14 14"><path d="M3 1 L5.5 1 L6.5 4 L5 5.3 C6 7.5 7 8.5 8.7 9.3 L10 8 L13 9 L13 11.5 C13 12.5 12 13 11 13 C5 12 2 9 1 3 C1 2 2 1 3 1Z" fill="#fff"/></svg></span>contact@brindlecovepc.com
  </div>
  <nav class="main-nav abs">
    <span class="active">HOME</span><span>PRACTICE AREAS</span><span>ATTORNEYS</span><span>RESULTS</span><span>FAQS</span><span>CONTACT US</span>
  </nav>
</header>

<section>
  <div class="hero abs" role="img" aria-label="Wooden judge's gavel resting on its sound block in warm light"></div>
  <h1 class="hero-title abs serif">WE PROVIDE LEGAL<br>HELP FOR</h1>
  <p class="hero-sub abs">We care about our clients and cultivating long-term relationships.</p>
  <div class="hero-btn btn abs">Read More</div>
</section>

<section>
  <h2 class="section-title abs" style="top:696px">WELCOME TO BRINDLE COVE</h2>
  <p class="section-sub abs" style="top:748px">The standard chunk of Lorem Ipsum used since the 1500s is reproduced below for those interested.</p>

  <div class="practice abs" style="left:57px">
    <svg width="80" height="90" viewBox="0 0 80 90"><polygon points="40,3 76,24 76,66 40,87 4,66 4,24" fill="none" stroke="#222" stroke-width="2"/><circle cx="40" cy="32" r="6" fill="none" stroke="#222" stroke-width="2"/><path d="M30 60 V46 H50 V60 M26 60 H54" fill="none" stroke="#222" stroke-width="2"/></svg>
    <div class="practice-rule"></div>
    <h3>Business Law</h3>
    <p>Attorney Maren Holt is ready to help<br>you reach positive outcomes<br>during mediation</p>
  </div>
  <div class="practice abs" style="left:335px">
    <svg width="80" height="90" viewBox="0 0 80 90"><polygon points="40,3 76,24 76,66 40,87 4,66 4,24" fill="none" stroke="#222" stroke-width="2"/><path d="M24 36 L40 26 L56 36 Z M27 40 V56 M35 40 V56 M45 40 V56 M53 40 V56 M23 60 H57" fill="none" stroke="#222" stroke-width="2"/></svg>
    <div class="practice-rule"></div>
    <h3>Civil Litigation</h3>
    <p>Attorney Maren Holt is ready to help<br>you reach positive outcomes<br>during mediation</p>
  </div>
  <div class="practice abs" style="left:607px">
    <svg width="80" height="90" viewBox="0 0 80 90"><polygon points="40,3 76,24 76,66 40,87 4,66 4,24" fill="none" stroke="#222" stroke-width="2"/><rect x="27" y="26" width="26" height="36" fill="none" stroke="#222" stroke-width="2"/><path d="M40 33 V53 M32 38 H48 M32 38 L29 46 H35 Z M48 38 L45 46 H51 Z M35 53 H45" fill="none" stroke="#222" stroke-width="1.6"/></svg>
    <div class="practice-rule"></div>
    <h3>Family Law</h3>
    <p>Attorney Maren Holt is ready to help<br>you reach positive outcomes<br>during mediation</p>
  </div>
  <div class="practice abs" style="left:887px">
    <svg width="80" height="90" viewBox="0 0 80 90"><polygon points="40,3 76,24 76,66 40,87 4,66 4,24" fill="none" stroke="#222" stroke-width="2"/><path d="M30 34 L40 24 L48 32 L38 42 Z M43 37 L55 49 M26 62 H46 M29 56 H43 V62" fill="none" stroke="#222" stroke-width="2"/></svg>
    <div class="practice-rule"></div>
    <h3>Criminal Law</h3>
    <p>Attorney Maren Holt is ready to help<br>you reach positive outcomes<br>during mediation</p>
  </div>
</section>

<section>
  <div class="consult-photo abs" role="img" aria-label="Smiling woman working on a laptop with colleagues in a bright office"></div>
  <div class="consult-panel abs"></div>
  <h2 class="consult-title abs serif">REQUEST A FREE CONSULTATION</h2>
  <p class="consult-sub abs">Perspiciatis unde omnis iste natus sit voluptatem accusantium doloremque.</p>
  <div class="field abs" style="left:643px;top:1329px;width:219px;height:43px"></div>
  <div class="field abs" style="left:882px;top:1329px;width:219px;height:43px"></div>
  <div class="field abs" style="left:643px;top:1393px;width:219px;height:43px"></div>
  <div class="field abs" style="left:882px;top:1393px;width:219px;height:43px"></div>
  <div class="field abs" style="left:643px;top:1456px;width:458px;height:92px"></div>
  <div class="send-btn abs">Send Request</div>
</section>

<section>
  <h2 class="section-title abs" style="top:1806px">WHAT OUR CUSTOMERS HAVE TO SAY</h2>
  <p class="section-sub abs" style="top:1866px">Collaboratively administrate empowered markets via plug-and-play networks. Dynamically procrastinate B2C users after installed base benefits.</p>

  <div class="t-card faded abs" style="left:72px;top:1995px;width:278px;height:175px;padding-top:16px">
    <div class="avatar" style="width:56px;height:56px" role="img" aria-label="Client portrait"></div>
    <p style="font-size:10px;line-height:15px;margin:10px 20px 0">Seamlessly connect user needs with practical service paths. Carefully grow lasting client relations and deliver steady outcomes.</p>
    <div class="t-name" style="width:148px;height:32px;font-size:11px;margin-top:12px">Dario Lenforth</div>
  </div>
  <div class="t-card faded abs" style="left:850px;top:1995px;width:278px;height:175px;padding-top:16px">
    <div class="avatar" style="width:56px;height:56px" role="img" aria-label="Client portrait"></div>
    <p style="font-size:10px;line-height:15px;margin:10px 20px 0">Seamlessly connect user needs with practical service paths. Carefully grow lasting client relations and deliver steady outcomes.</p>
    <div class="t-name" style="width:148px;height:32px;font-size:11px;margin-top:12px">Dario Lenforth</div>
  </div>
  <div class="t-card abs" style="left:408px;top:1955px;width:394px;height:245px;padding-top:18px">
    <div class="avatar" style="width:82px;height:82px" role="img" aria-label="Client portrait"></div>
    <p style="font-size:13.5px;line-height:22px;margin-top:14px">Dramatically maintain clicks-and-mortar solutions<br>without functional solutions. Completely<br>synergize resource taxing relationships<br>premier niche markets</p>
  </div>
  <div class="t-name abs" style="left:511px;top:2180px;width:187px;height:40px;font-size:15px">Dario Lenforth</div>
  <div class="dots abs"><span class="dot on"></span><span class="dot"></span><span class="dot"></span><span class="dot"></span><span class="dot"></span></div>
</section>

<section>
  <div class="call-band abs"></div>
  <svg class="call-red abs" viewBox="0 0 440 120" width="440" height="120"><polygon points="0,0 368,0 440,120 0,120" fill="#e2232a"/></svg>
  <svg class="abs" style="left:68px;top:2438px" width="36" height="36" viewBox="0 0 14 14"><path d="M3 1 L5.5 1 L6.5 4 L5 5.3 C6 7.5 7 8.5 8.7 9.3 L10 8 L13 9 L13 11.5 C13 12.5 12 13 11 13 C5 12 2 9 1 3 C1 2 2 1 3 1Z" fill="#fff"/></svg>
  <div class="call-help abs">FOR ANY HELP OR<br>QUERIES</div>
  <div class="call-now abs">Call Us Now On <b>0400-5550193</b></div>
  <div class="join-btn abs">JOIN US</div>
</section>

<footer>
  <div class="site-footer abs"></div>
  <div class="f-head abs" style="left:70px">CONTACTS</div>
  <div class="f-head abs" style="left:342px">LATEST NEWS</div>
  <div class="f-head abs" style="left:613px">ABOUT</div>
  <div class="f-head abs" style="left:882px">QUICK CONTACT</div>

  <div class="f-row abs" style="left:72px;top:2613px"><svg width="14" height="14" viewBox="0 0 14 14" style="margin-top:4px"><path d="M3 1 L5.5 1 L6.5 4 L5 5.3 C6 7.5 7 8.5 8.7 9.3 L10 8 L13 9 L13 11.5 C13 12.5 12 13 11 13 C5 12 2 9 1 3 C1 2 2 1 3 1Z" fill="#ccc"/></svg>(800) 555 01 87</div>
  <div class="f-row abs" style="left:72px;top:2659px"><svg width="16" height="14" viewBox="0 0 16 14" style="margin-top:4px"><rect x="1" y="2" width="14" height="10" fill="none" stroke="#ccc" stroke-width="1.3"/><path d="M1 2 L8 8 L15 2" fill="none" stroke="#ccc" stroke-width="1.3"/></svg>info@brindlecovepc.com</div>
  <div class="f-row abs" style="left:72px;top:2705px"><svg width="12" height="16" viewBox="0 0 12 16" style="margin-top:3px"><path d="M6 1 C3 1 1 3 1 6 C1 10 6 15 6 15 C6 15 11 10 11 6 C11 3 9 1 6 1Z" fill="#ccc"/><circle cx="6" cy="6" r="2" fill="#161616"/></svg><span>48 Alder Lane, Fresno, California<br>93701, USA</span></div>
  <div class="socials abs"><span></span><span></span><span></span><span></span><span></span><span></span></div>

  <div class="news abs" style="top:2612px">This is a Audio post Type<i>January 5, 2016</i></div>
  <div class="news abs" style="top:2666px">This is a Gallery post Type<i>January 5, 2016</i></div>
  <div class="news abs" style="top:2720px">This is a Quote post Type<i>January 5, 2016</i></div>
  <div class="news abs" style="top:2773px">Post Video<i>October 2, 2015</i></div>

  <p class="about abs">Cum sociis natoque penatibus et magnis dis parturient montes, nascetur ridiculus mus. Etiam imperdiet. Ut sollicitudin sem sit amet ipsum. In id dui. Pellentesque sapien.</p>
  <div class="about-brand abs"><span></span>CounselHub</div>

  <div class="qf abs" style="top:2610px;height:36px">YOUR NAME</div>
  <div class="qf abs" style="top:2656px;height:36px">YOUR EMAIL</div>
  <div class="qf abs" style="top:2702px;height:90px">MESSAGE...</div>
  <div class="f-send btn abs">Send</div>

  <div class="f-line abs"></div>
  <div class="copy abs">© 2016 WWW.BRINDLECOVEPC.COM RIGHT RESERVED.</div>
</footer>

</body>
</html>
```